Landscape design build company door flyer

I would like this flyer to convey a high-level of professionalism for a company that is excellent with communication with their clients as well as a company that does incredible installations

Went on vacation/holiday

```html
<!DOCTYPE html>
<html lang="en">
<head>
<meta charset="utf-8">
<title>Stillwater Outdoor Co. – Door Flyer</title>
<link href="https://fonts.googleapis.com/css2?family=Marcellus&family=Montserrat:wght@500;600;700&display=swap" rel="stylesheet">
<style>
  :root {
    --gold: #fdb913;
    --navy: #0d3547;
    --white: #ffffff;
    --stage: #0a1917;
    --photo-sky: #9fb6c8;
    --photo-stone: #6e7479;
    --photo-wood: #b07a45;
  }
  html, body {
    margin: 0;
    width: 1200px;
    height: 1200px;
    overflow: hidden;
    background: var(--stage);
  }
  .flyer {
    position: absolute;
    left: 40px;
    top: 204px;
    width: 1120px;
    height: 792px;
    display: block;
  }
  .brand-name { font-family: "Montserrat", sans-serif; font-weight: 700; font-size: 24px; fill: var(--navy); }
  .headline { font-family: "Marcellus", serif; font-size: 24px; fill: var(--gold); }
  .intro { font-family: "Montserrat", sans-serif; font-weight: 500; font-size: 12.5px; fill: var(--white); }
  .section-title { font-family: "Marcellus", serif; font-size: 22px; fill: var(--gold); }
  .service { font-family: "Montserrat", sans-serif; font-weight: 500; font-size: 16px; fill: var(--white); }
  .cta { font-family: "Montserrat", sans-serif; font-weight: 700; font-size: 18px; fill: var(--navy); }
</style>
</head>
<body>
<svg class="flyer" viewBox="0 0 1093 773" xmlns="http://www.w3.org/2000/svg">
  <defs>
    <linearGradient id="grad-house" x1="0" y1="0" x2="0" y2="1">
      <stop offset="0" stop-color="#8e9aa6"/>
      <stop offset="0.45" stop-color="#6b4e3a"/>
      <stop offset="1" stop-color="#77797b"/>
    </linearGradient>
    <linearGradient id="grad-pavilion" x1="0" y1="0" x2="0" y2="1">
      <stop offset="0" stop-color="var(--photo-sky)"/>
      <stop offset="0.4" stop-color="var(--photo-wood)"/>
      <stop offset="1" stop-color="var(--photo-stone)"/>
    </linearGradient>
    <clipPath id="flyer-clip"><rect width="1093" height="773"/></clipPath>
  </defs>

  <g clip-path="url(#flyer-clip)">
    <rect class="bg" width="1093" height="773" fill="var(--gold)"/>

    <path class="swoosh-white" d="M0,218 C160,195 390,165 480,80 C520,40 545,12 575,0 L760,0 L760,320 L0,330 Z" fill="var(--white)"/>

    <path d="M0,322 C120,300 260,318 420,400 L420,430 C260,350 120,332 0,352 Z" fill="var(--gold)"/>
    <path d="M0,330 C120,310 260,326 420,408" fill="none" stroke="var(--navy)" stroke-width="6"/>

    <path class="base-navy" d="M0,352 C150,330 300,380 460,460 C600,530 720,620 900,640 C990,648 1050,620 1093,590 L1093,773 L0,773 Z" fill="var(--navy)"/>

    <path d="M620,560 C720,620 820,655 930,650 C1000,645 1050,600 1093,560 L1093,590 C1050,620 990,648 900,640 C800,632 710,600 620,560 Z" fill="var(--white)"/>
    <path d="M600,560 C720,640 830,670 940,665 C1010,660 1060,610 1093,575" fill="none" stroke="var(--gold)" stroke-width="5"/>

    <circle cx="756" cy="291" r="298" fill="var(--white)"/>
    <circle cx="756" cy="291" r="280" fill="none" stroke="var(--navy)" stroke-width="2.5"/>
    <circle class="photo" cx="756" cy="291" r="256" fill="url(#grad-house)" role="img" aria-label="Photo: front yard with stone block retaining wall, paver steps and walkway to a grey house"/>

    <circle cx="181" cy="326" r="134" fill="#cfd8dd"/>
    <circle class="photo" cx="181" cy="326" r="124" fill="url(#grad-pavilion)" role="img" aria-label="Photo: timber pavilion with stone outdoor kitchen on a paver patio"/>
    <circle cx="391" cy="316" r="120" fill="#f6e3a8"/>
    <circle class="photo" cx="391" cy="316" r="110" fill="url(#grad-pavilion)" role="img" aria-label="Photo: covered patio with wood posts and outdoor lounge seating"/>

    <!-- brand name -->
    <g class="brand">
      <circle cx="72" cy="131" r="12" fill="var(--navy)"/>
      <text class="brand-name" x="94" y="140">Stillwater Outdoor Co.</text>
    </g>

    <text class="headline" x="34" y="505">It’s Time to Discover Your Zen</text>
    <text class="intro" x="35" y="524">From vision to reality, let us bring your dream</text>
    <text class="intro" x="35" y="542">outdoor space to life.</text>

    <text class="section-title" x="41" y="582">Our Services</text>
    <line x1="186" y1="574" x2="391" y2="574" stroke="var(--gold)" stroke-width="1.2"/>

    <g class="service-list">
      <rect x="40" y="604" width="18" height="18" fill="var(--gold)"/>
      <text class="service" x="68" y="619">Pools</text>
      <rect x="40" y="637" width="18" height="18" fill="var(--gold)"/>
      <text class="service" x="68" y="652">Paver Patios</text>
      <rect x="40" y="668" width="18" height="18" fill="var(--gold)"/>
      <text class="service" x="68" y="683">Paver Driveways</text>
      <rect x="40" y="700" width="18" height="18" fill="var(--gold)"/>
      <text class="service" x="68" y="715">Retaining Walls</text>

      <rect x="226" y="603" width="18" height="18" fill="var(--gold)"/>
      <text class="service" x="257" y="618">Decks &amp; Railings</text>
      <rect x="226" y="636" width="18" height="18" fill="var(--gold)"/>
      <text class="service" x="257" y="652">Outdoor Lighting</text>
      <rect x="226" y="669" width="18" height="18" fill="var(--gold)"/>
      <text class="service" x="257" y="685">Firepits and Fireplaces</text>
    </g>

    <g class="cta-bar">
      <rect x="498" y="697" width="555" height="38" rx="19" fill="var(--gold)"/>
      <rect x="655" y="697" width="180" height="38" fill="var(--white)"/>
      <path d="M828,697 h10 a19,19 0 0 0 0,38 h-10 Z" fill="var(--white)"/>
      <text class="cta" x="508" y="723">Call Us Now!</text>
      <circle cx="654" cy="716" r="11" fill="var(--white)" stroke="var(--gold)" stroke-width="2"/>
      <path d="M649,710 l3,-1 2,4 -2,1.5 c1,2 2.5,3.5 4.5,4.5 l1.5,-2 4,2 -1,3 c-6,0 -12,-6 -12,-12 z" fill="var(--navy)"/>
      <text class="cta" x="672" y="722">(555) 014-2290</text>
      <text class="cta" x="838" y="724">Get a Free Estimate</text>
    </g>
  </g>
</svg>
</body>
</html>
```